Zelcor Stationary

Design the stationary of Zelcor Promotion Group.

Zelcor is a BTL company, BTL meaning "below the line". In other words Zelcor is a Promotional Marketing company (the company that design the brands promotional activities).

The design should transmit creativity, agility, boldness.

I need:
* Bis Card
* Letter head
* Envelopes, both vertical and horizontal (for legal size), and letter envelope
* Folders
* PPT template (Title page and regular page)
* CD slip (CD envelope)
* ID card (employee card)

And what ever else you want to throw in.
Updates

Guys,

Something I missed from the brief.   The predominat color should be RED.

Also, have fun and play with the exclamation mark (!) of the logo. 

Hi guys, more comments:

Remember that Zelcor is a "creativity" agency, not in the advertising side but on the promotional side, and that should reflect on the stationary.

 I want a bold design.  Bold and yet crisp.

 

Guys, i just uploaded the Logo in AI format.

I Also uploaded the actual Zelcor Bis Card, wich I like.  So I will like to see some designs with that bis card approach.

Guys, I am so sorry, but I notice in your last post that I upladed a wrong design ("13154_marketing_group_zelcor_brief225630.ai").  The problem was that I asked the designer the file in AI format and he send me thw wrong file, and since I dont have Illustrator I could not verify it.

The differences are minor, I just already ask him the correct one (similar to the EPS file).

Sorry                                   

Just post the correct AI file : "Zelcor Logo.ai"

Reason: I'm expecting more designs to choose from and also I wont be available tomorrow to decide.

Reason: Sorry guys, but we are not there yet!

Target Market(s)

Marketing directors, Marketing Managers

Industry/Entity Type

Legal

Requirements
Must have
• Must work with the logo attached.
The predominat color should be RED.
Play and have fun with the exclamation mark (!).
Should not have
• * No old fonts

Should not be:
* boring
* Informal
* rigid

```html
<!DOCTYPE html>
<html lang="en">
<head>
<meta charset="utf-8">
<title>Zelcor Promotion Group – Letterhead</title>
<link rel="stylesheet" href="https://fonts.googleapis.com/css2?family=Poppins:wght@400;600;700&display=swap">
<style>
  :root {
    --red: #b4202d;
    --red-deep: #6d1a22;
    --red-line: #9a1f2a;
    --ink: #1a1a1a;
    --paper: #ffffff;
    --ghost: #e3e3e3;
    --ghost-accent: #f6d6d8;
  }
  * { margin: 0; padding: 0; box-sizing: border-box; }
  html, body { width: 848px; height: 1200px; overflow: hidden; background: var(--paper); }
  .letterhead {
    position: relative;
    width: 848px;
    height: 1200px;
    background: var(--paper);
    font-family: "Poppins", sans-serif;
    color: var(--ink);
    overflow: hidden;
  }
  .rule-top, .rule-bottom {
    position: absolute;
    left: 0;
    width: 848px;
    height: 8px;
    background: repeating-linear-gradient(90deg, var(--red-line) 0 44px, transparent 44px 49px);
  }
  .rule-top { top: 0; }
  .rule-bottom { bottom: 0; }
  .rule-side {
    position: absolute;
    right: 6px;
    top: 54px;
    width: 4px;
    height: 1122px;
    background: repeating-linear-gradient(180deg, var(--red-line) 0 26px, transparent 26px 30px);
  }
  .brand-tab {
    position: absolute;
    left: 20px;
    top: 0;
    width: 316px;
    height: 151px;
    border-radius: 0 0 34px 34px;
    background: linear-gradient(100deg, var(--red) 0%, #8f1d27 60%, var(--red-deep) 100%);
    color: var(--paper);
  }
  .brand-name {
    position: absolute;
    left: 40px;
    top: 30px;
    font-size: 44px;
    font-weight: 700;
    line-height: 1;
  }
  .brand-sub {
    position: absolute;
    left: 42px;
    top: 86px;
    font-size: 11px;
    font-weight: 600;
    letter-spacing: 3px;
    line-height: 1;
  }
  .brand-dot {
    position: absolute;
    left: 252px;
    top: 50px;
    width: 30px;
    height: 30px;
    border-radius: 50%;
    background: var(--paper);
  }
  .brand-url {
    position: absolute;
    left: 0;
    width: 100%;
    top: 116px;
    text-align: center;
    font-size: 16px;
    font-weight: 600;
    letter-spacing: 3.2px;
    line-height: 1;
  }
  .ghost-name {
    position: absolute;
    left: 166px;
    top: 948px;
    font-size: 140px;
    font-weight: 700;
    line-height: 1;
    color: var(--ghost);
  }
  .ghost-sub {
    position: absolute;
    left: 170px;
    top: 1094px;
    font-size: 28px;
    font-weight: 400;
    line-height: 1;
    letter-spacing: 10px;
    color: var(--ghost);
  }
  .ghost-dot {
    position: absolute;
    left: 652px;
    top: 1048px;
    width: 84px;
    height: 84px;
    border-radius: 50%;
    background: var(--ghost-accent);
  }
  .contact {
    position: absolute;
    left: 0;
    width: 848px;
    top: 1150px;
    text-align: center;
    font-size: 14px;
    font-weight: 700;
    line-height: 16px;
    letter-spacing: 1.4px;
  }
</style>
</head>
<body>
  <main class="letterhead">
    <div class="rule-top"></div>
    <div class="rule-side"></div>

    <header class="brand-tab">
      <div class="brand-name">Zelcor</div>
      <div class="brand-sub">PROMOTION GROUP</div>
      <div class="brand-dot"></div>
      <div class="brand-url">www.zelcor.com.do</div>
    </header>

    <div class="ghost-name" aria-hidden="true">zelcor</div>
    <div class="ghost-sub" aria-hidden="true">PROMOTION GROUP</div>
    <div class="ghost-dot" aria-hidden="true"></div>

    <footer class="contact">
      <p>Calle 12 No. 48 Ens Los Pinos, Santo Domingo, Republica Dominicana</p>
      <p>Tel 809.555.0142&nbsp;&nbsp;&nbsp;Fax: 809.555.0187</p>
    </footer>

    <div class="rule-bottom"></div>
  </main>
</body>
</html>
```